A5 Personal trainer profile for corbell vitality

I need a A5 Landscape profile designed for the company I work for. Company name is Corbell Vitality. The profile is for personal trainers to let people know:

1. Brief description of themselves
2. Qualifications

A picture will be required on the right hand side of the profile. Corbell Vitality colours are green and white.

The Corbell Vitality Logo in the boarder of the example included must remain. We are looking for a clinical and professional design.

Industry/Entity Type

Health

```html
<!DOCTYPE html>
<html lang="en">
<head>
<meta charset="utf-8">
<title>Personal Trainer Profile – Corbell Vitality</title>
<link rel="stylesheet" href="https://fonts.googleapis.com/css2?family=Source+Sans+3:wght@400;600;700&display=swap">
<style>
  :root {
    --lime: #8dc63f;
    --forest: #00743a;
    --forest-deep: #006530;
    --name-green: #2f6b58;
    --ink: #333333;
    --white: #ffffff;
    --backdrop: #dedede;
  }
  * { box-sizing: border-box; margin: 0; padding: 0; }
  html, body {
    width: 1200px; height: 1200px; overflow: hidden;
    background: var(--backdrop);
    font-family: "Source Sans 3", "Myriad Pro", Arial, sans-serif;
  }
  .profile-card {
    position: absolute; left: 50px; top: 211px;
    width: 1100px; height: 778px;
    background: var(--white);
    overflow: hidden;
  }
  .card-shapes { position: absolute; inset: 0; }
  .header-band-text { position: absolute; left: 34px; top: 12px; }
  .role-title {
    color: var(--white); font-weight: 600; font-size: 46px; line-height: 1.1;
  }
  .trainer-name {
    color: var(--name-green); font-weight: 700; font-size: 76px;
    line-height: 1; letter-spacing: 1px; margin-top: 2px;
  }
  .brand {
    position: absolute; right: 22px; top: 20px;
    display: flex; align-items: center; gap: 8px;
    color: var(--forest); font-weight: 600; font-size: 31px;
  }
  .brand-mark { width: 24px; height: 24px; background: var(--forest); }
  .section-heading {
    position: absolute; left: 28px;
    color: var(--forest); font-weight: 700; line-height: 1;
  }
  .help-heading { top: 176px; font-size: 50px; }
  .clients-heading { top: 364px; font-size: 41px; }
  .qual-heading { top: 548px; font-size: 55px; }
  .tick-list { position: absolute; list-style: none; color: var(--ink); }
  .tick-list li { position: relative; padding-left: 26px; line-height: 23.6px; white-space: nowrap; }
  .tick-list li::before {
    content: ""; position: absolute; left: 4px; top: 4px;
    width: 7px; height: 13px;
    border-right: 3px solid var(--forest); border-bottom: 3px solid var(--forest);
    transform: rotate(40deg);
  }
  .help-list { left: 30px; top: 232px; font-size: 19.5px; }
  .qual-list { left: 34px; top: 618px; font-size: 19.5px; }
  .qual-list li { padding-left: 34px; }
  .qual-list li::before { border-color: var(--lime); }
  .qual-list li.continued::before { display: none; }
  .testimonial {
    position: absolute; left: 30px; top: 424px; width: 420px;
    font-size: 18.5px; line-height: 23.6px; color: var(--ink);
  }
  .testimonial span { display: block; white-space: nowrap; }
  .testimonial .justified { text-align: justify; text-align-last: justify; white-space: normal; }
</style>
</head>
<body>
  <main class="profile-card">
    <svg class="card-shapes" width="1100" height="778" viewBox="0 0 1100 778">
      <defs>
        <linearGradient id="portrait-tone" x1="0" y1="0" x2="0" y2="1">
          <stop offset="0" stop-color="#ffffff"/>
          <stop offset="0.45" stop-color="#eef3e2"/>
          <stop offset="1" stop-color="#cfe89c"/>
        </linearGradient>
      </defs>
      <rect class="header-band" x="0" y="0" width="900" height="154" fill="var(--lime)"/>
      <rect x="0" y="154" width="900" height="4" fill="var(--forest)"/>
      <path role="img" aria-label="Portrait photograph of the personal trainer in a green polo shirt"
            d="M 680 748 Q 680 150 890 0 L 1100 0 L 1100 748 Z" fill="url(#portrait-tone)"/>
      <path d="M 638 748 Q 640 130 830 0 L 890 0 Q 680 150 680 748 Z" fill="var(--lime)"/>
      <path d="M 602 748 Q 592 120 760 0 L 830 0 Q 640 130 638 748 Z" fill="var(--forest-deep)"/>
      <rect x="0" y="748" width="1100" height="30" fill="var(--forest-deep)"/>
    </svg>

    <div class="brand"><span class="brand-mark"></span>Corbell Vitality</div>

    <header class="header-band-text">
      <p class="role-title">Personal Trainer</p>
      <h1 class="trainer-name">KOFI MENSAH</h1>
    </header>

    <h2 class="section-heading help-heading">How I can help you?</h2>
    <ul class="tick-list help-list">
      <li>Reduce body fat&nbsp; and increase body definition</li>
      <li>Increase stamina, improve agility and speed</li>
      <li>Increase strength and size</li>
      <li>Plyometric training and conditioning</li>
      <li>Flexibility and core strength</li>
    </ul>

    <h2 class="section-heading clients-heading">What my clients say bout me?</h2>
    <p class="testimonial">
      <span>"With Kofi my training is always challenging and fun.</span>
      <span>I don’t remember a session to be boring or repetitive.</span>
      <span class="justified">In short time I improved my core strength and</span>
      <span class="justified">flexibility. I can run 10k without stopping. It is</span>
      <span>amazing improvement. " Rachel Dunmore</span>
    </p>

    <h2 class="section-heading qual-heading">Qualifications</h2>
    <ul class="tick-list qual-list">
      <li>Advanced Circuit Training</li>
      <li>Advanced Diploma in Personal Training - Level 3 KFTA Registered</li>
      <li>Fitness Instructor - Level 2 KFTA Registered</li>
      <li>Also qualified in – Suspension training, Studio Cycling,</li>
      <li class="continued">Sports Nutrition,&nbsp; Weight Management</li>
    </ul>
  </main>
</body>
</html>
```